New Innovative Product needs a new business card design

We need a business card design for a new product line based in Michigan called "Lendwise Tailwind." We are a credit company by nature however this product should have a clean, simple, "zorvik-esque" feel. We have a few tag lines we use that could or could not be used...."All Referral Roads Lead to You" we use the attached pic in much or our marketing and also use both a white and/or black logo. Also attached.

We want the image attached on the card in some form or another- the grass/sky image.

Reason: We are extending to go over options with management- (expiring on weekend)

Reason: To finalize our design pick. We will be in touch with the designer of choice within the next day or so...the last few entries have been great- Sorry for the delay.

Reason: Working with a couple different designs trying to get finalized

Reason: Final in the workds

Marketing

• We want the image attached on the card in some form or another- the grass/sky image.

```html
<!DOCTYPE html>
<html lang="en">
<head>
<meta charset="utf-8">
<title>Lendwise Tailwind – Business Card</title>
<link rel="stylesheet" href="https://fonts.googleapis.com/css2?family=Open+Sans:wght@400;600;700;800&display=swap">
<style>
  :root {
    --backdrop: #e9e9e7;
    --card-white: #ffffff;
    --brand-green: #1e8f4e;
    --ink: #111111;
    --logo-ink: #2b2b2b;
    --text-light: #ffffff;
  }
  * { box-sizing: border-box; margin: 0; padding: 0; }
  html, body {
    width: 1200px; height: 546px; overflow: hidden;
    background: var(--backdrop);
    font-family: "Open Sans", Arial, sans-serif;
  }
  .stage { position: relative; width: 1200px; height: 546px; }
  .card {
    position: absolute; top: 124px;
    width: 520px; height: 297px;
    background: var(--card-white);
    box-shadow: 0 6px 18px rgba(0,0,0,0.18);
    overflow: hidden;
  }
  .card--front { left: 50px; }
  .card--back { left: 630px; }
  .card__bands { position: absolute; inset: 0; width: 100%; height: 100%; }

  .wordmark {
    position: absolute; left: 0; right: 0;
    display: flex; align-items: center; justify-content: center; gap: 12px;
    color: var(--logo-ink); font-weight: 600; letter-spacing: -0.5px;
  }
  .wordmark__square { background: var(--brand-green); flex: none; }
  .card--front .wordmark { top: 58px; font-size: 34px; }
  .card--front .wordmark__square { width: 30px; height: 30px; }
  .card--back .wordmark { top: 62px; font-size: 40px; }
  .card--back .wordmark__square { width: 36px; height: 36px; }

  .holder {
    position: absolute; right: 42px; top: 162px;
    text-align: right; color: var(--text-light);
  }
  .holder__name { font-weight: 800; font-size: 17px; letter-spacing: 0.3px; }
  .holder__title { font-size: 13px; margin-top: -2px; }
  .holder-tab {
    position: absolute; right: 14px; top: 160px;
    width: 16px; height: 28px; background: var(--ink);
  }

  .contact-rail {
    position: absolute; left: 10px; top: 212px;
    width: 24px; height: 78px; background: var(--ink);
    display: flex; flex-direction: column; align-items: center; justify-content: space-around;
    padding: 4px 0;
  }
  .contact-rail svg { width: 14px; height: 14px; }
  .contact-list {
    position: absolute; left: 44px; top: 212px;
    color: var(--text-light); font-size: 10.5px; line-height: 1.3;
  }
  .contact-list li { list-style: none; }
  .contact-list .contact__phone { margin-top: 3px; }
  .contact-list .contact__email { margin-top: 12px; }
  .contact-list .contact__address { margin-top: 8px; }

  .tagline {
    position: absolute; left: 0; right: 0; top: 198px;
    text-align: center; color: var(--text-light);
    font-weight: 700; font-size: 23px; letter-spacing: -0.3px;
  }
</style>
</head>
<body>
<main class="stage">

  <section class="card card--front" aria-label="Business card front">
    <svg class="card__bands" viewBox="0 0 520 297" preserveAspectRatio="none" aria-hidden="true">
      <path d="M0,150 Q250,200 520,128 L520,297 L0,297 Z" fill="var(--brand-green)"/>
      <path d="M0,150 Q250,200 520,128" fill="none" stroke="var(--ink)" stroke-width="3"/>
    </svg>

    <div class="wordmark"><span class="wordmark__square"></span><span>Lendwise Tailwind</span></div>

    <div class="holder-tab"></div>
    <div class="holder">
      <p class="holder__name">MARLO VENTER</p>
      <p class="holder__title">Product Manager</p>
    </div>

    <div class="contact-rail" aria-hidden="true">
      <svg viewBox="0 0 14 14"><rect x="3.5" y="1" width="7" height="12" rx="1.2" fill="none" stroke="#fff" stroke-width="1.3"/></svg>
      <svg viewBox="0 0 14 14"><rect x="1" y="3" width="12" height="8" fill="none" stroke="#fff" stroke-width="1.2"/><path d="M1,3 L7,8 L13,3" fill="none" stroke="#fff" stroke-width="1.2"/></svg>
      <svg viewBox="0 0 14 14"><path d="M7,13 C3,8 2.5,6.5 2.5,5.2 A4.5,4.5 0 0 1 11.5,5.2 C11.5,6.5 11,8 7,13 Z" fill="#fff"/><circle cx="7" cy="5.2" r="1.7" fill="var(--ink)"/></svg>
    </div>
    <ul class="contact-list">
      <li class="contact__phone">1-555-204-7781</li>
      <li class="contact__email">mventer@ledgerbrookcredit.com</li>
      <li class="contact__address">2710 W. Maple Ridge Rd.<br>Holloway, MI 48000</li>
    </ul>
  </section>

  <section class="card card--back" aria-label="Business card back">
    <svg class="card__bands" viewBox="0 0 520 297" preserveAspectRatio="none" aria-hidden="true">
      <path d="M0,148 Q260,205 520,150 L520,297 L0,297 Z" fill="var(--brand-green)"/>
      <path d="M0,148 Q260,205 520,150" fill="none" stroke="var(--ink)" stroke-width="3"/>
    </svg>

    <div class="wordmark"><span class="wordmark__square"></span><span>Lendwise Tailwind</span></div>

    <p class="tagline">Every Referral Path Starts with You</p>
  </section>

</main>
</body>
</html>
```